*YO!!! Designers Needed!!* Front Page Cover Needed for a $$Billion Dollar$$ Company

We are a manufacturer of aluminum electrolytic capacitors. We are looking to create a front page cover that will be used on our annual report. We are a publicly listed company and work with many Brellmont 500 companies, so your work will be viewed by the BIG GUNS and EXECUTIVES around the WORLD! If selected, you may be selected for additional work.

The front page cover should be unique. If elegance, modern, bling, and creativity somehow got together and had a child, that's what the cover page would look like!

Inspired Examples attached. Check them out!

www.kovantro.com

Font styles to use
Sans Serif

Requirements
Must have
• 1. Must include the attached logo. Logo size, color, and placement are at your discretion.

2. Should include the text, '2020 Annual Report'

3. The design should incorporate the use of foil and/or be embossed. The foil can be part of the design or can be the full page. See various examples attached for reference.

4. Shall be in A4 size and vertical orientation.
Nice to have
• Feel free to add any icons or stock photos (for example capacitors or circuit boards) if needed.

Be creative here and don't be afraid to be bold! The end product will be printed and budget is not a limiting factor, so feel free to make it extravagant if needed.

Our slogan is "Think Ahead". This slogan can or cannot be part of the theme.

```html
<!DOCTYPE html>
<html lang="en">
<head>
<meta charset="utf-8">
<title>Kovantro 2020 Annual Report Cover</title>
<link href="https://fonts.googleapis.com/css2?family=Josefin+Sans:wght@300;400;700&display=swap" rel="stylesheet">
<style>
  :root {
    --foil-light: #f4f4f5;
    --foil-mid: #d9dadc;
    --foil-dark: #b9bbbe;
    --navy: #1e3263;
    --board-green: #2f7a3e;
    --board-dark: #1d3f26;
    --ink: #0d0d0f;
  }
  html, body {
    margin: 0;
    padding: 0;
    width: 848px;
    height: 1200px;
    overflow: hidden;
    background: #ffffff;
  }
  .cover {
    position: relative;
    width: 848px;
    height: 1200px;
    overflow: hidden;
    font-family: "Josefin Sans", sans-serif;
    color: var(--ink);
    background:
      radial-gradient(ellipse 420px 300px at 560px 330px, rgba(255,255,255,0.85), transparent 70%),
      radial-gradient(ellipse 360px 420px at 180px 1050px, rgba(255,255,255,0.6), transparent 70%),
      radial-gradient(ellipse 500px 260px at 720px 760px, rgba(160,162,166,0.35), transparent 70%),
      radial-gradient(ellipse 300px 300px at 820px 80px, rgba(170,172,176,0.35), transparent 70%),
      linear-gradient(160deg, var(--foil-mid) 0%, var(--foil-light) 35%, var(--foil-dark) 60%, var(--foil-light) 82%, var(--foil-mid) 100%);
  }
  .cover-art {
    position: absolute;
    inset: 0;
    width: 848px;
    height: 1200px;
  }
  .brand {
    position: absolute;
    right: 54px;
    top: 56px;
    text-align: right;
  }
  .brand-name {
    display: block;
    font-weight: 700;
    font-size: 56px;
    line-height: 1;
    letter-spacing: 0.5px;
    color: var(--ink);
  }
  .brand-slogan {
    display: block;
    margin-top: 18px;
    font-weight: 700;
    font-size: 15px;
    letter-spacing: 0.5px;
    color: var(--ink);
  }
  .report-title {
    position: absolute;
    left: 524px;
    top: 912px;
    margin: 0;
    font-weight: 400;
    line-height: 1;
  }
  .report-year {
    display: block;
    font-weight: 300;
    font-size: 56px;
    letter-spacing: 0.5px;
  }
  .report-label {
    display: block;
    font-size: 66px;
    line-height: 0.97;
    letter-spacing: -1.5px;
  }
  .report-year + .report-label {
    margin-top: 8px;
  }
</style>
</head>
<body>
  <main class="cover">
    <svg class="cover-art" viewBox="0 0 848 1200" xmlns="http://www.w3.org/2000/svg">
      <defs>
        <linearGradient id="board-tones" x1="0" y1="0" x2="1" y2="1">
          <stop offset="0" stop-color="#4b4f4c"/>
          <stop offset="0.35" stop-color="var(--board-green)"/>
          <stop offset="0.7" stop-color="#3c8a49"/>
          <stop offset="1" stop-color="var(--board-dark)"/>
        </linearGradient>
      </defs>
      <polygon class="circuit-photo" role="img"
               aria-label="Close-up photograph of a green circuit board with capacitors and a microchip"
               points="0,142 428,598 0,1055" fill="url(#board-tones)"/>
      <polygon class="chevron-band"
               points="97,168 530,598 97,1029 97,912 413,598 97,285" fill="var(--navy)"/>
    </svg>

    <header class="brand">
      <span class="brand-name">Kovantro</span>
      <span class="brand-slogan">BUILD FORWARD.</span>
    </header>

    <h1 class="report-title">
      <span class="report-year">2020</span>
      <span class="report-label">ANNUAL</span>
      <span class="report-label">REPORT</span>
    </h1>
  </main>
</body>
</html>
```